Harborlight Equity Corporate Profile

Redesign Corporate Profile with special attention to Cover, Dividers, Introduction of professional images, icons, colors, formatting among others. To visually enhance the 24 pages to give it a financial look with a young and fresh angle.
The PPT is a corporate profile which is a presentation about the company, its key milestones along with specific key case studies.
Images related to Dubai city, millennial consumer, globalization, technology should be included.
Target Market(s)
Investors, Brand Owners, Shareholders, Employees
Industry/Entity Type
Investment Advisory
Requirements
Must have
- Maintain current content and section structure
- Enhance cover, dividers
- Add professional images
- Enhance graphs and charts
- Add info-graphics

```html
<!DOCTYPE html>
<html lang="en">
<head>
<meta charset="utf-8">
<title>Harborlight Equity — Corporate Profile Slides</title>
<link href="https://fonts.googleapis.com/css2?family=Roboto:wght@300;400;500;700&family=Merriweather:wght@300;400&display=swap" rel="stylesheet">
<style>
:root{
  --stage:#5f5f5f;
  --red:#d71f26;
  --red-dark:#b3141b;
  --ink:#222;
  --dark:#4a4a4a;
  --grey:#8a8a8a;
  --muted:#9a9a9a;
  --line:#e4e4e4;
  --white:#fff;
}
*{box-sizing:border-box;margin:0;padding:0}
html,body{width:1200px;height:690px;overflow:hidden;background:var(--stage)}
body{font-family:"Roboto",Arial,sans-serif;color:var(--ink)}
.sheet{display:grid;grid-template-columns:repeat(3,1fr);grid-template-rows:repeat(3,1fr);gap:16px;padding:10px 12px;width:1200px;height:690px}
.slide{position:relative;overflow:hidden;background:var(--white)}
.brand{position:absolute;top:10px;right:12px;font-family:"Merriweather",Georgia,serif;font-size:8px;color:var(--red);letter-spacing:.5px}
.footer-url{position:absolute;left:7px;bottom:6px;font-family:"Merriweather",Georgia,serif;font-size:6px;color:var(--muted)}
.page-no{position:absolute;right:9px;bottom:6px;font-size:6px;color:var(--muted)}
.kicker{position:absolute;left:12px;top:6px;font-size:4.5px;letter-spacing:1px;color:#c4c4c4;text-transform:uppercase}
.slide-title{position:absolute;left:12px;top:14px;font-size:10px;letter-spacing:1px;color:var(--ink)}
.slide-title::after{content:"";display:block;width:18px;height:2px;background:var(--red);margin-top:5px}
.tiny{font-size:4px;line-height:6.4px;color:var(--grey)}

/* cover */
.cover{background:#050505;color:var(--white);display:flex;flex-direction:column;align-items:center;justify-content:center;font-family:"Merriweather",Georgia,serif}
.cover-name{font-size:13px;letter-spacing:1.5px;margin-bottom:18px}
.cover-tag{font-size:8.5px}
.cover-tag em{font-style:normal;color:var(--red)}

/* quote */
.quote{background:var(--red);color:var(--white);text-align:center;font-family:"Merriweather",Georgia,serif;padding:0 50px;display:flex;flex-direction:column;align-items:center;justify-content:center}
.quote-name{font-size:13px;letter-spacing:1px;margin-bottom:12px}
.quote p{font-size:7px;line-height:11.5px}
.quote-sign{font-size:8px;margin-top:10px}

/* photo slides */
.photo-people{background:linear-gradient(135deg,#9a9a9a,#5a5a5a 55%,#3f3f3f)}
.photo-text{position:absolute;top:92px;left:40px;right:30px;text-align:center;font-family:"Merriweather",Georgia,serif;font-size:7px;line-height:11.5px;color:#eee}
.photo-people .footer-url,.photo-people .page-no{color:#ddd}
.photo-people .rule{position:absolute;left:6px;right:6px;bottom:17px;height:1px;background:rgba(255,255,255,.35)}

.divider{background:linear-gradient(180deg,#e04a4f,#c1141c 55%,#8e0d12)}
.divider .brand{color:var(--white)}
.divider-title{position:absolute;top:86px;width:100%;text-align:center;color:var(--white);font-size:17px;font-weight:300;letter-spacing:2px}
.divider p{position:absolute;top:113px;left:40px;right:40px;text-align:center;color:var(--white);font-family:"Merriweather",Georgia,serif;font-size:6.5px;line-height:10.5px}

.details{display:grid;grid-template-columns:178px 1fr}
.details-photo{background:linear-gradient(120deg,#eee,#777 45%,#2b2b2b)}
.details-panel{background:var(--red);color:var(--white);padding:28px 14px 0 19px;position:relative}
.details-panel .brand{color:var(--white)}
.details-panel h3{font-weight:300;font-size:10px;letter-spacing:.8px;margin-bottom:12px}
.details-panel p{font-family:"Merriweather",Georgia,serif;font-size:6.6px;line-height:11.5px;margin-bottom:10px}

/* agenda grid */
.agenda-grid{position:absolute;left:28px;right:30px;top:44px;display:grid;grid-template-columns:repeat(3,1fr);column-gap:20px;row-gap:20px}
.agenda-item header{display:flex;align-items:center;gap:6px;margin-bottom:10px;font-size:6px}
.dot{width:19px;height:19px;border-radius:50%;display:flex;align-items:center;justify-content:center;flex:none}
.dot svg{width:9px;height:9px;fill:var(--white)}
.dot.red{background:var(--red)}.dot.grey{background:#8a8a8a}.dot.dark{background:var(--dark)}
.agenda-item header.red{color:var(--red)}

/* icons */
.icon-row{position:absolute;left:18px;right:30px;top:48px;display:grid;grid-template-columns:repeat(4,1fr);column-gap:12px;text-align:center}
.big-dot{width:38px;height:38px;margin:0 auto 9px;border-radius:50%;display:flex;align-items:center;justify-content:center}
.big-dot svg{width:15px;height:15px;fill:var(--white)}
.big-dot.red{background:var(--red)}.big-dot.dark{background:var(--dark)}
.icon-label{font-size:5.5px;margin-bottom:7px}
.icon-label.red{color:var(--red)}

/* chevron agenda */
.steps{position:absolute;left:54px;right:40px;top:44px;display:flex;flex-direction:column;gap:9px}
.step{display:flex;gap:8px;align-items:flex-start}
.step svg{width:52px;height:27px;flex:none}
.step svg text{font-size:11px;fill:var(--white);font-family:"Roboto",Arial,sans-serif}
.step h4{font-size:5.5px;font-weight:500;margin-bottom:2px}

/* data slide */
.map{position:absolute;left:36px;top:44px;width:130px;height:98px;background:linear-gradient(160deg,#cfcfcf,#a9a9a9);border-radius:30% 40% 45% 30%}
.badge{position:absolute;left:70px;top:92px;background:var(--red);color:var(--white);font-size:11px;padding:3px 12px;border-radius:12px;box-shadow:0 0 0 2px #f2f2f2}
.users{position:absolute;left:46px;top:164px;display:flex;gap:10px}
.user{display:flex;gap:3px;align-items:center}
.user .dot{width:14px;height:14px}
.user b{display:block;font-size:7px;color:var(--red);font-weight:500}
.user small{display:block;font-size:3.5px;color:var(--grey)}
.data-col{position:absolute;left:193px;right:28px;top:42px}
.data-col h4{font-size:5px;font-weight:500;margin-bottom:3px}
.data-col .vline{position:absolute;left:-6px;top:100px;width:1px;height:30px;background:#ccc}
.chart{display:block;margin:6px 0 4px}
.chart text{font-size:4px;fill:var(--grey);font-family:"Roboto",Arial,sans-serif}
</style>
</head>
<body>
<main class="sheet">

  <section class="slide cover">
    <div class="cover-name">HARBORLIGHT EQUITY</div>
    <div class="cover-tag">Global Growth with <em>Local Expertise</em></div>
  </section>

  <section class="slide quote">
    <div class="quote-name">Harborlight Equity</div>
    <p>"Our investment approach focuses on partnering with brands which are in the rollout phase that require capital and local expertise to successfully enter and grow in internation markets"</p>
    <div class="quote-sign">Marisa Kovacs &nbsp;||&nbsp; Founder &amp; CEO</div>
  </section>

  <section class="slide photo-people" role="img" aria-label="Black and white photo of a group of smiling young friends taking a selfie">
    <div class="brand">Harborlight Equity</div>
    <div class="photo-text">Liquorice chupa chups &nbsp;cake applicake apple pie cupcake brownie bear claw<br>Liquorice chupa chups &nbsp;cake applicake apple pie cupcake brownie bear claw<br>Liquorice chupa chups &nbsp;cake applicake apple pie cupcake brownie bear claw<br>Liquorice chupa chups &nbsp;cake applicake</div>
    <div class="rule"></div>
    <div class="footer-url">www.harborlightpartners.ae</div>
    <div class="page-no">01</div>
  </section>

  <section class="slide">
    <div class="kicker">Section One</div>
    <h2 class="slide-title">Our Agenda</h2>
    <div class="brand">Harborlight Equity</div>
    <div class="agenda-grid">
      <article class="agenda-item"><header class="red"><span class="dot red"><svg viewBox="0 0 10 10"><rect x="1" y="1" width="8" height="8" rx="1.5"/></svg></span>Creative Strategy</header><p class="tiny">Focused plans that turn local insight into lasting regional growth.</p></article>
      <article class="agenda-item"><header class="red"><span class="dot red"><svg viewBox="0 0 10 10"><rect x="1" y="1.5" width="8" height="5.5"/><rect x="3.5" y="7.5" width="3" height="1.2"/></svg></span>Employee Desktop</header><p class="tiny">Flexible tools that keep every team connected and productive daily.</p></article>
      <article class="agenda-item"><header class="red"><span class="dot red"><svg viewBox="0 0 10 10"><circle cx="3" cy="4" r="2"/><circle cx="7" cy="4" r="2"/><rect x="1.5" y="4" width="1.5" height="3"/><rect x="5.5" y="4" width="1.5" height="3"/></svg></span>Business Plan</header><p class="tiny">Clear roadmaps with milestones, budgets and measurable returns for partners.</p></article>
      <article class="agenda-item"><header><span class="dot grey"><svg viewBox="0 0 10 10"><path d="M5 .5 9 2v3c0 2.5-2 4-4 4.5C3 9 1 7.5 1 5V2z"/></svg></span>System Protection</header><p class="tiny">Robust controls that protect assets, data and investor confidence.</p></article>
      <article class="agenda-item"><header><span class="dot dark"><svg viewBox="0 0 10 10"><rect x=".5" y="3" width="9" height="4.5" rx="2.2"/></svg></span>Fun Games</header><p class="tiny">Team events that build trust, energy and shared company culture.</p></article>
      <article class="agenda-item"><header><span class="dot dark"><svg viewBox="0 0 10 10"><rect x="4.2" y="1" width="1.6" height="5"/><path d="M2 4.5h6L5 7.5z"/><rect x="1.5" y="8" width="7" height="1"/></svg></span>Data Analysis</header><p class="tiny">Sharp market data that guides every decision we make together.</p></article>
    </div>
    <div class="footer-url">www.harborlightpartners.ae</div>
    <div class="page-no">01</div>
  </section>

  <section class="slide">
    <div class="kicker">Section One</div>
    <h2 class="slide-title">Creative Visual Icons</h2>
    <div class="brand">Harborlight Equity</div>
    <div class="icon-row">
      <article><div class="big-dot red"><svg viewBox="0 0 10 10"><rect x=".5" y="1.5" width="9" height="6"/><rect x="3.5" y="8" width="3" height="1"/></svg></div><div class="icon-label red">Desktop Application</div><p class="tiny">Digital platforms built for fast onboarding and smooth daily use by clients.</p></article>
      <article><div class="big-dot red"><svg viewBox="0 0 10 10"><ellipse cx="5" cy="6" rx="2.5" ry="3"/><circle cx="5" cy="2.5" r="1.3"/><rect x="0.5" y="5" width="9" height=".8"/></svg></div><div class="icon-label red">Business Strategy</div><p class="tiny">Market entry plans shaped by research, local partners and clear targets.</p></article>
      <article><div class="big-dot dark"><svg viewBox="0 0 10 10"><path d="M5 .5 9 2v3c0 2.5-2 4-4 4.5C3 9 1 7.5 1 5V2z"/></svg></div><div class="icon-label">Sales Booster</div><p class="tiny">Proven campaigns that lift revenue across new channels and regions quickly.</p></article>
      <article><div class="big-dot dark"><svg viewBox="0 0 10 10"><path d="M9.5.5C6 .8 3.5 3 2.5 6l1.5 1.5C7 6.5 9.2 4 9.5.5zM2 6.5.5 8l1 .5.5 1 1.5-1.5z"/></svg></div><div class="icon-label">Concept &amp; Ideas</div><p class="tiny">Fresh concepts tested early and refined with brand owners and investors.</p></article>
    </div>
    <div class="footer-url">www.harborlightpartners.ae</div>
    <div class="page-no">01</div>
  </section>

  <section class="slide divider" role="img" aria-label="Red-toned photo of the Dubai skyline">
    <div class="brand">Harborlight Equity</div>
    <h2 class="divider-title">IMAGE &nbsp;SECTION DIVIDER</h2>
    <p>"Our investment approach focuses on partnering with brands which are in the rollout phase that require capital and local expertise to successfully enter and grow in internation markets"</p>
  </section>

  <section class="slide details">
    <div class="details-photo" role="img" aria-label="Black and white photo looking up a glass office tower"></div>
    <div class="details-panel">
      <div class="brand">Harborlight Equity</div>
      <h3>IMAGE &nbsp;SECTION Details</h3>
      <p>Our investment approach focuses on partnering with brands which are in the rollout phase that require capital and local expertise to successfully enter and grow in internation markets.</p>
      <p>Our investment approach focuses on partnering with brands which are in the rollout phase that require capital and local expertise to successfully enter and grow in internation markets"</p>
    </div>
  </section>

  <section class="slide">
    <div class="kicker">Section One</div>
    <h2 class="slide-title">Our Agenda</h2>
    <div class="brand">Harborlight Equity</div>
    <div class="steps">
      <article class="step"><svg viewBox="0 0 52 27"><polygon points="0,0 44,0 52,13.5 44,27 0,27 7,13.5" fill="#d71f26"/><text x="24" y="18">1</text></svg><div><h4>Creative Strategy</h4><p class="tiny">We map each brand's strengths and match them with the right regional markets and partners.</p></div></article>
      <article class="step"><svg viewBox="0 0 52 27"><polygon points="0,0 44,0 52,13.5 44,27 0,27 7,13.5" fill="#9a9a9a"/><text x="24" y="18">2</text></svg><div><h4>Boost Sales</h4><p class="tiny">Targeted launches, pricing and distribution plans that grow sales in the first key year.</p></div></article>
      <article class="step"><svg viewBox="0 0 52 27"><polygon points="0,0 44,0 52,13.5 44,27 0,27 7,13.5" fill="#6e6e6e"/><text x="24" y="18">3</text></svg><div><h4>Global Brand Strategy</h4><p class="tiny">A consistent brand voice across borders, adapted to local culture, language and buyer habits.</p></div></article>
      <article class="step"><svg viewBox="0 0 52 27"><polygon points="0,0 44,0 52,13.5 44,27 0,27 7,13.5" fill="#4a4a4a"/><text x="24" y="18">4</text></svg><div><h4>Business Strategy</h4><p class="tiny">Capital, governance and growth planning that keep every venture steady and ready to scale.</p></div></article>
    </div>
    <div class="footer-url">www.harborlightpartners.ae</div>
    <div class="page-no">01</div>
  </section>

  <section class="slide">
    <div class="kicker">Section One</div>
    <h2 class="slide-title">Creative Visual Design</h2>
    <div class="brand">Harborlight Equity</div>
    <div class="map" role="img" aria-label="Grey map of North America"></div>
    <div class="badge">359 M</div>
    <div class="users">
      <div class="user"><span class="dot red"><svg viewBox="0 0 10 10"><circle cx="5" cy="2" r="1.5"/><rect x="3.5" y="4" width="3" height="5"/></svg></span><div><b>1.908 K</b><small>Male User</small></div></div>
      <div class="user"><span class="dot red"><svg viewBox="0 0 10 10"><circle cx="5" cy="2" r="1.5"/><path d="M5 3.8 7.5 8h-5z"/></svg></span><div><b>2.074 K</b><small>Female User</small></div></div>
    </div>
    <div class="data-col">
      <h4>Data Analysis</h4>
      <p class="tiny">Regional user growth measured across five years of steady expansion in key markets.</p>
      <svg class="chart" viewBox="0 0 150 70" width="150" height="70">
        <g stroke="#e6e6e6" stroke-width=".5"><line x1="10" y1="4" x2="148" y2="4"/><line x1="10" y1="15" x2="148" y2="15"/><line x1="10" y1="26" x2="148" y2="26"/><line x1="10" y1="37" x2="148" y2="37"/><line x1="10" y1="48" x2="148" y2="48"/><line x1="10" y1="59" x2="148" y2="59"/></g>
        <text x="2" y="6">5</text><text x="2" y="17">4</text><text x="2" y="28">3</text><text x="2" y="39">2</text><text x="2" y="50">1</text><text x="2" y="61">0</text>
        <rect x="20" y="22" width="13" height="37" fill="#d71f26"/>
        <rect x="46" y="31" width="13" height="28" fill="#d71f26"/>
        <rect x="72" y="21" width="13" height="38" fill="#d71f26"/>
        <rect x="98" y="7" width="13" height="52" fill="#4a4a4a"/>
        <rect x="124" y="18" width="13" height="41" fill="#4a4a4a"/>
        <text x="19" y="68">2010</text><text x="45" y="68">2011</text><text x="71" y="68">2012</text><text x="97" y="68">2013</text><text x="123" y="68">2014</text>
      </svg>
      <div class="vline"></div>
      <p class="tiny">Figures show active users per year, in millions, across our partner brand portfolio.</p>
    </div>
    <div class="footer-url">www.harborlightpartners.ae</div>
    <div class="page-no">01</div>
  </section>

</main>
</body>
</html>
```